New Business Card Design Project

I need a clean, professional business card. I'd like it to have some color, but not be wild. We do technology consulting and we have clients large and small who trust us with some of their most important data and projects. Simple but not boring should drive all design proposals. Multicolored and two sided, but with a matte finish, I think.
For more on tone, check out our website: http://quorvantis.example

Target Market(s)

Upper management of respected businesses. Tech savvy, but not "hipster".

Industry/Entity Type

Business

Requirements
Must have
• Files need to be provided in .eps and in .pdf in a manner that allows for easy updates.
Must have Name, Title, Phone, Email, Twitter, Website
Nice to have
• Logo/Name shouldn't be too big. One thing I've read several places is that the bigger the logo, the smaller the brand. A good article on dos and don'ts here: http://www.brindlepost.example/2011/02/business-card-experience.html

```html
<!DOCTYPE html>
<html lang="en">
<head>
<meta charset="utf-8">
<title>Quorvantis Business Card – Front and Back</title>
<link href="https://fonts.googleapis.com/css2?family=Arimo:wght@400;700&family=Didact+Gothic&display=swap" rel="stylesheet">
<style>
  :root {
    --stage-top: #767676;
    --stage-bottom: #cccccc;
    --leaf-light: #88a64a;
    --leaf-dark: #779642;
    --olive-band: #869a4d;
    --leaf-band: #9ab845;
    --teal: #4a9bae;
    --paper: #ffffff;
    --paper-shade: #e9e8e8;
    --ink: #2a2f24;
    --ink-soft: #555a58;
    --label: #ffffff;
    --label-dark: #111111;
  }
  * { box-sizing: border-box; margin: 0; padding: 0; }
  html, body { width: 1200px; height: 1200px; overflow: hidden; }
  body {
    background: linear-gradient(180deg, var(--stage-top) 0%, #7d7d7d 45%, var(--stage-bottom) 100%);
    font-family: "Arimo", Arial, sans-serif;
  }
  .canvas { position: relative; width: 1200px; height: 1200px; }

  .card {
    position: absolute;
    left: 114px;
    width: 908px;
    height: 521px;
    border-radius: 6px;
    overflow: hidden;
  }
  .card--front { top: 56px; background: linear-gradient(180deg, var(--leaf-light) 0%, var(--leaf-dark) 80%); }
  .card--back { top: 618px; background: linear-gradient(180deg, var(--paper) 0%, var(--paper-shade) 70%); }

  .card__accent { position: absolute; left: 0; right: 0; }
  .card--front .card__accent {
    top: 330px;
    height: 120px;
    background: linear-gradient(180deg, var(--leaf-dark) 0%, var(--olive-band) 35%, var(--teal) 75%, var(--paper) 100%);
  }
  .card__footer { position: absolute; left: 0; right: 0; top: 450px; bottom: 0; background: var(--paper); }
  .card--back .card__accent {
    top: 290px;
    bottom: 0;
    background: linear-gradient(180deg, var(--paper-shade) 0%, var(--leaf-band) 25%, var(--leaf-band) 45%, var(--teal) 70%, var(--teal) 100%);
  }

  .side-label {
    position: absolute;
    font-family: "Arimo", Arial, sans-serif;
    font-weight: 700;
    font-size: 45px;
    letter-spacing: 1px;
  }
  .side-label--front { left: 1030px; top: 304px; color: var(--label); }
  .side-label--back { left: 1043px; top: 836px; color: var(--label-dark); }

  .embossed {
    color: var(--ink);
    text-shadow: 0 1px 0 rgba(255,255,255,0.25), 0 -1px 0 rgba(0,0,0,0.35);
  }
  .identity {
    position: absolute;
    left: 480px;
    width: 410px;
    top: 28px;
    text-align: center;
    font-weight: 700;
    line-height: 1.05;
  }
  .identity__name { font-size: 40px; }
  .identity__title { font-size: 34px; margin-top: 2px; }

  .contacts { position: absolute; left: 40px; top: 134px; list-style: none; }
  .contact {
    display: flex;
    align-items: center;
    height: 44px;
    margin-bottom: 30px;
    font-size: 35px;
  }
  .contact:nth-child(3) { margin-top: -6px; }
  .contact__icon { width: 54px; height: 40px; margin-right: 12px; flex: none; }

  .brand {
    position: absolute;
    display: flex;
    align-items: center;
    font-family: "Didact Gothic", "Century Gothic", sans-serif;
    color: var(--ink-soft);
    letter-spacing: 2px;
  }
  .brand__mark { background: var(--teal); flex: none; }
  .brand--small { left: 12px; top: 472px; font-size: 29px; }
  .brand--small .brand__mark { width: 18px; height: 18px; margin-right: 12px; }
  .brand--large { left: 258px; top: 142px; font-size: 50px; }
  .brand--large .brand__mark { width: 32px; height: 32px; margin-right: 20px; }

  .web {
    position: absolute;
    right: 31px;
    top: 478px;
    font-size: 29px;
    font-weight: 700;
  }
</style>
</head>
<body>
<main class="canvas">

  <section class="card card--front" aria-label="Card front">
    <div class="card__accent" role="img" aria-label="Decorative flowing bands in olive and teal"></div>
    <div class="card__footer"></div>

    <div class="identity embossed">
      <p class="identity__name">YOUR NAME HERE</p>
      <p class="identity__title">TITLE</p>
    </div>

    <ul class="contacts">
      <li class="contact embossed">
        <svg class="contact__icon" viewBox="0 0 54 40" aria-hidden="true">
          <rect x="2" y="4" width="50" height="32" fill="none" stroke="var(--ink)" stroke-width="3"/>
          <path d="M2,4 L27,24 L52,4 M2,36 L21,19 M52,36 L33,19" fill="none" stroke="var(--ink)" stroke-width="3"/>
        </svg>
        <span>j.hale@quorvantis.example</span>
      </li>
      <li class="contact embossed">
        <svg class="contact__icon" viewBox="0 0 54 48" aria-hidden="true">
          <path d="M3,14 C3,2 51,2 51,14 L51,19 L40,19 L40,13 L14,13 L14,19 L3,19 Z" fill="var(--ink)"/>
          <path d="M12,20 L42,20 L48,46 L6,46 Z" fill="var(--ink)"/>
          <circle cx="27" cy="33" r="8" fill="var(--leaf-light)"/>
          <circle cx="27" cy="33" r="3.5" fill="var(--ink)"/>
        </svg>
        <span>+1 (800) 555-0142</span>
      </li>
      <li class="contact embossed">
        <svg class="contact__icon" viewBox="0 0 54 40" aria-hidden="true">
          <circle cx="27" cy="20" r="16" fill="var(--ink)"/>
        </svg>
        <span>@QUORVANTIS</span>
      </li>
    </ul>

    <div class="brand brand--small">
      <span class="brand__mark"></span>
      <span class="brand__name">QUORVANTIS</span>
    </div>
    <p class="web embossed">www.quorvantis.example</p>
  </section>

  <p class="side-label side-label--front">FRONT</p>

  <section class="card card--back" aria-label="Card back">
    <div class="card__accent" role="img" aria-label="Decorative flowing bands in green and teal"></div>
    <div class="brand brand--large">
      <span class="brand__mark"></span>
      <span class="brand__name">QUORVANTIS</span>
    </div>
  </section>

  <p class="side-label side-label--back">BACK</p>

</main>
</body>
</html>
```